Real Estate Managemene Company Needs Business Card Design

We have a logo design and just need business cards made now for our business. Please use PDF logo # 3.

Card with Information to be attached shortly.

The card is used for a real estate management company. We will need to add four other employees and their cards.

Industry/Entity Type

Real Estate

Contact Information for Business Card

Tariq Hamdan
President
3187 Thornwick Avenue
Suite C
Ashgrove Park, WI 53921
Phone 555.417.2286
Fax 555.417.2287
Cell 555.473.8062
vantorp@mailbreeze.net

Once design is approved we will have four other employees
Omar Hamdan
Operations Manager

Nadia Hamdan
Administrative Manager

Faz Hamdan
Principal

We would need to take out the cell # 555.473.8062 out for the remaining three cards.

Requirements
Must have
• Please use logo attached

```html
<!DOCTYPE html>
<html lang="en">
<head>
<meta charset="utf-8">
<title>Wrenfield Property Group – Business Cards</title>
<link rel="stylesheet" href="https://fonts.googleapis.com/css2?family=Open+Sans:wght@400;600;700&display=swap">
<style>
  :root {
    --backdrop: #e9e6e1;
    --card-white: #f7f7f6;
    --card-grey: #6e6f72;
    --card-grey-light: #8a8b8e;
    --brand-red: #d8283a;
    --text-light: #f2f2f2;
    --shadow: rgba(0, 0, 0, 0.22);
  }
  * { margin: 0; padding: 0; box-sizing: border-box; }
  html, body { width: 1200px; height: 780px; overflow: hidden; }
  body {
    background: var(--backdrop);
    font-family: "Open Sans", Arial, sans-serif;
    position: relative;
  }
  .card {
    position: absolute;
    top: 230px;
    width: 540px;
    height: 310px;
    border-radius: 3px;
    box-shadow: 0 10px 26px var(--shadow);
    overflow: hidden;
  }
  .card--info { left: 50px; display: flex; }
  .card--brand {
    left: 610px;
    background: linear-gradient(135deg, var(--card-grey-light), var(--card-grey));
    display: flex; align-items: center; justify-content: center;
  }
  .info__brand-side {
    width: 46%;
    background: var(--card-white);
    display: flex; align-items: center; justify-content: center;
    border-right: 3px solid var(--brand-red);
  }
  .info__details {
    flex: 1;
    background: linear-gradient(160deg, var(--card-grey-light), var(--card-grey));
    padding: 40px 24px 0 30px;
    color: var(--text-light);
  }
  .brand-name {
    display: flex; align-items: center; gap: 10px;
    color: var(--brand-red);
    font-weight: 700;
    font-size: 19px;
    line-height: 1.2;
    text-transform: uppercase;
    letter-spacing: 0.5px;
  }
  .brand-name__square {
    width: 26px; height: 26px; flex: none;
    background: var(--brand-red);
  }
  .card--brand .brand-name { font-size: 24px; }
  .card--brand .brand-name__square { width: 32px; height: 32px; }
  .person__name {
    color: var(--brand-red);
    font-weight: 700;
    font-size: 21px;
    line-height: 1.2;
    text-transform: uppercase;
    letter-spacing: 0.5px;
  }
  .person__title { font-size: 14px; margin-top: 2px; }
  .address { font-size: 13px; line-height: 1.55; margin-top: 24px; }
  .contacts { list-style: none; margin-top: 10px; font-size: 13px; }
  .contacts li { display: flex; align-items: center; gap: 8px; line-height: 1.55; }
  .contacts svg { width: 15px; height: 15px; flex: none; }
</style>
</head>
<body>
  <section class="card card--info" aria-label="Business card, contact side">
    <div class="info__brand-side">
      <div class="brand-name"><span class="brand-name__square"></span><span>Wrenfield<br>Property Group</span></div>
    </div>
    <div class="info__details">
      <p class="person__name">Tariq Hamdan</p>
      <p class="person__title">President</p>
      <p class="address">3187 Thornwick Avenue, Suite C<br>Ashgrove Park, WI 53921</p>
      <ul class="contacts">
        <li><svg viewBox="0 0 16 16"><rect width="16" height="16" fill="#d8283a"/><path d="M4 3.5l2 0 1 2.5-1.3 1a6 6 0 0 0 2.8 2.8l1-1.3 2.5 1v2c0 .6-.5 1-1 1A8 8 0 0 1 3 4.5c0-.5.4-1 1-1z" fill="#fff"/></svg>555.417.2286</li>
        <li><svg viewBox="0 0 16 16"><rect width="16" height="16" fill="#d8283a"/><rect x="5" y="3" width="6" height="4" fill="#fff"/><rect x="3" y="7" width="10" height="5" fill="#fff"/><rect x="5" y="9" width="6" height="1" fill="#d8283a"/></svg>555.417.2287</li>
        <li><svg viewBox="0 0 16 16"><rect width="16" height="16" fill="#d8283a"/><rect x="5" y="2.5" width="6" height="11" rx="1" fill="#fff"/><rect x="6" y="4" width="4" height="6" fill="#d8283a"/></svg>555.473.8062</li>
        <li><svg viewBox="0 0 16 16"><rect width="16" height="16" fill="#d8283a"/><rect x="3" y="4.5" width="10" height="7" fill="#fff"/><path d="M3 4.5l5 4 5-4" fill="none" stroke="#d8283a" stroke-width="1"/></svg>vantorp@mailbreeze.net</li>
      </ul>
    </div>
  </section>

  <section class="card card--brand" aria-label="Business card, brand side">
    <div class="brand-name"><span class="brand-name__square"></span><span>Wrenfield<br>Property Group</span></div>
  </section>
</body>
</html>
```